An e-flyer for an exotic car and fine wine club.

This is the first meeting of Birchwell Motor Society and includes several businesses. Their logos should be featured at the bottom. It should be sleek, elegant and simple featuring a photo of an Corvane Lestrel R7 as well as my logo (I will provide photos). The flyer needs to look professional and appeal to billionaires.
The text should read:
Birchwell Motor society presents
Fast Cars and Fine Wine (but not while driving)
Hosted by Harlow Gem Vault
Bring your best car(s) and join us to enjoy the party with sommelier selected wines, the best classic and modern cars and hors d'oeuvre catered by Penrose's Clam House. Live DJ.
August 26th 3-6 p.m.
This event is gratis.
RSVP to dana@birchwellmotors.example for address and details

Target Market(s)
Very wealthy exotic car owners
Industry/Entity Type
Car Club, Fine Wines.
Requirements
Must have
- Style, panache, elegance, sleekness, simplicity. I like the idea of a black or dark flyer with a consistent color scheme.
Nice to have
- I want the flyer to be simple and sleek, feature an Corvane Lestrel R7 as the eye catcher, Birchwell Motor Society logo featured prominently on the top, and the other business logos on the bottom.
Should not have
- It must not be too noisy or busy.

```html
<!DOCTYPE html>
<html lang="en">
<head>
<meta charset="UTF-8">
<title>Fast Cars and Fine Wine — Birchwell Motor Society</title>
<link rel="stylesheet" href="https://fonts.googleapis.com/css2?family=Rubik:ital,wght@0,800;1,800&family=Montserrat:wght@400;500;700&display=swap">
<style>
  :root {
    --stage: #3b3638;
    --paper: #f1eff3;
    --paper-shade: #e2e0e5;
    --sky: #d3d3d9;
    --asphalt: #9c9ea3;
    --car-red: #b51f27;
    --red: #d9222a;
    --red-deep: #c81d24;
    --orange: #ee6a1f;
    --yellow: #f4d31c;
    --ink: #1f1f22;
    --ink-soft: #3a3a3e;
    --white: #ffffff;
  }
  * { box-sizing: border-box; margin: 0; padding: 0; }
  html, body { width: 1200px; height: 800px; overflow: hidden; }
  body {
    background: var(--stage);
    display: flex;
    align-items: center;
    justify-content: center;
    font-family: "Montserrat", sans-serif;
  }
  .flyer {
    position: relative;
    width: 540px;
    height: 764px;
    background: linear-gradient(180deg, var(--paper) 0%, var(--paper-shade) 100%);
    overflow: hidden;
  }
  .hero-photo {
    position: absolute;
    left: 0; right: 0;
    top: 340px; height: 262px;
    background: linear-gradient(160deg, var(--sky) 0%, var(--sky) 22%, var(--car-red) 50%, var(--car-red) 58%, var(--asphalt) 86%, var(--asphalt) 100%);
  }
  .brand {
    position: absolute;
    top: 62px; left: 0; right: 0;
    display: flex;
    align-items: center;
    justify-content: center;
    gap: 12px;
  }
  .brand-mark {
    width: 34px; height: 34px;
    border-radius: 50%;
    background: var(--ink);
  }
  .brand-name {
    font-weight: 700;
    font-size: 22px;
    letter-spacing: 3px;
    text-transform: uppercase;
    color: var(--ink);
    line-height: 1.1;
  }
  .presents {
    position: absolute;
    top: 128px; left: 0; right: 0;
    text-align: center;
    font-size: 15px;
    letter-spacing: 7px;
    color: var(--ink-soft);
  }
  .headline {
    position: absolute;
    top: 158px; left: 0; right: 0;
    text-align: center;
    font-family: "Rubik", sans-serif;
    font-weight: 800;
    font-style: italic;
    font-size: 50px;
    line-height: 1.0;
    text-transform: uppercase;
    color: var(--red);
  }
  .tagline {
    position: absolute;
    top: 270px; left: 0; right: 0;
    text-align: center;
    font-size: 22px;
    color: var(--ink);
  }
  .host {
    position: absolute;
    top: 302px; left: 0; right: 0;
    text-align: center;
    font-size: 20px;
    color: var(--red);
  }
  .host strong { font-weight: 700; color: var(--orange); }
  .date-box {
    position: absolute;
    top: 578px; right: 36px;
    width: 192px; height: 104px;
    border-radius: 10px;
    background: var(--red-deep);
    display: flex;
    flex-direction: column;
    align-items: center;
    justify-content: center;
    font-family: "Rubik", sans-serif;
    font-weight: 800;
    font-size: 21px;
    line-height: 1.12;
    text-transform: uppercase;
    color: var(--white);
    z-index: 2;
  }
  .date-box .date-day { color: var(--yellow); }
  .details {
    position: absolute;
    top: 614px; left: 36px;
    width: 280px;
    color: var(--ink);
  }
  .details-copy {
    font-size: 11.5px;
    line-height: 1.45;
    font-weight: 500;
  }
  .details-copy .accent { color: var(--red); font-weight: 700; }
  .gratis {
    margin-top: 10px;
    font-size: 14px;
    font-weight: 700;
    letter-spacing: 0.3px;
  }
  .rsvp {
    margin-top: 8px;
    font-size: 12.5px;
    line-height: 1.4;
  }
  .rsvp a { color: var(--red); text-decoration: none; }
  .partners {
    position: absolute;
    top: 696px; right: 30px;
    width: 204px;
    display: flex;
    justify-content: space-between;
    align-items: center;
    gap: 10px;
  }
  .partner-name {
    font-weight: 700;
    font-size: 11px;
    line-height: 1.15;
    text-transform: uppercase;
    text-align: center;
  }
  .partner-name.wine-shop { color: var(--ink); }
  .partner-name.host-vault { color: var(--orange); }
  .edge-band {
    position: absolute;
    right: 0; bottom: 0;
  }
  .edge-band.bottom {
    left: 0; height: 6px;
    background: linear-gradient(90deg, var(--red) 0%, var(--orange) 55%, var(--orange) 100%);
  }
  .edge-band.side {
    width: 6px; height: 300px;
    background: linear-gradient(180deg, var(--yellow) 0%, var(--orange) 60%, var(--orange) 100%);
  }
</style>
</head>
<body>
  <main class="flyer">
    <div class="hero-photo" role="img" aria-label="Photograph of a red Corvane Lestrel R7 classic coupe on a track under an overcast sky"></div>

    <header class="brand">
      <span class="brand-mark"></span>
      <span class="brand-name">Birchwell Motor Society</span>
    </header>
    <p class="presents">PRESENTS</p>

    <h1 class="headline">Fast Cars and<br>Fine Wine</h1>
    <p class="tagline">(but not while driving)</p>
    <p class="host">Hosted by <strong>Harlow Gem Vault</strong></p>

    <div class="date-box">
      <span class="date-month">August</span>
      <span class="date-day">26th, 2023</span>
      <span class="date-time">3-6 p.m.</span>
    </div>

    <section class="details">
      <p class="details-copy">Bring your best car(s) &amp; join us to enjoy the party with sommelier selected wines, the best classic &amp; modern cars &amp; hors d'oeuvre catered by Penrose's Clam House. <span class="accent">Live DJ.</span></p>
      <p class="gratis">THIS EVENT IS GRATIS</p>
      <p class="rsvp">RSVP to <a href="mailto:dana@birchwellmotors.example">dana@birchwellmotors.example</a><br>for address and details</p>
    </section>

    <footer class="partners">
      <span class="partner-name wine-shop">Marisol<br>Cellar Shop</span>
      <span class="partner-name host-vault">Harlow<br>Gem Vault</span>
    </footer>

    <div class="edge-band side"></div>
    <div class="edge-band bottom"></div>
  </main>
</body>
</html>
```